Corvale Homes

To produce a business card design for our newly established house building and development company, We have had a logo design done please see attached, our slogan is "building your home sweet home"
Contact Information for Business Card
Adress on card needs to Read - 58 Elmsworth Lane, Kettering, Northamptonshire NN16 4QT. Director name Dean Vascotti
Requirements
Must have
- Web adress is www.corvale-homes.co.uk
- Email address is info@corvale-homes.co.uk
- phone number 07700 900417

```html
<!DOCTYPE html>
<html lang="en">
<head>
<meta charset="utf-8">
<title>Corvale Homes – Business Card</title>
<link rel="stylesheet" href="https://fonts.googleapis.com/css2?family=Arimo:wght@400;700&family=Lato:wght@400&display=swap">
<style>
  :root {
    --band: #f9fafc;
    --stage: #ffffff;
    --brand-green: #8cc63f;
    --green-edge: #6f9f32;
    --card-white: #ffffff;
    --card-edge: #a9a9a9;
    --ink-dark: #3d3d3d;
    --ink-text: #333333;
    --on-green: #ffffff;
  }
  * { margin: 0; padding: 0; box-sizing: border-box; }
  html, body { width: 1200px; height: 1200px; overflow: hidden; }
  body { position: relative; background: var(--band); font-family: "Arimo", Arial, sans-serif; }

  .stage { position: absolute; left: 0; top: 360px; width: 1200px; height: 480px; background: var(--stage); }

  .card { position: absolute; top: 457px; width: 510px; height: 291px; }

  .card--front { left: 86px; background: var(--brand-green); border: 1px solid var(--green-edge);
    display: flex; align-items: center; justify-content: center; }
  .front-name { color: var(--on-green); font-family: "Arimo", Arial, sans-serif; font-weight: 700;
    font-size: 38px; letter-spacing: 1px; text-transform: uppercase; }

  .card--back { left: 634px; background: var(--card-white); border: 1px solid var(--card-edge); }

  .holder { position: absolute; left: 23px; top: 38px; color: var(--ink-dark); }
  .holder-name { font-weight: 700; font-size: 20px; line-height: 24px; text-transform: uppercase; }
  .holder-role { font-size: 18px; line-height: 22px; }

  .back-brand { position: absolute; right: 22px; top: 60px; color: var(--ink-dark);
    font-weight: 700; font-size: 16px; letter-spacing: .5px; text-transform: uppercase; }

  .contact { position: absolute; left: 22px; top: 183px; list-style: none;
    font-family: "Lato", Calibri, sans-serif; font-size: 16.5px; line-height: 22px; color: var(--ink-text); }
</style>
</head>
<body>
  <div class="stage"></div>

  <section class="card card--front">
    <span class="front-name">Corvale Homes</span>
  </section>

  <section class="card card--back">
    <div class="holder">
      <p class="holder-name">Dean Vascotti</p>
      <p class="holder-role">Director</p>
    </div>
    <span class="back-brand">Corvale Homes</span>
    <ul class="contact">
      <li>Phone: 07700 900417</li>
      <li>info@corvale-homes.co.uk</li>
      <li>www.corvale-homes.co.uk</li>
      <li>58 Elmsworth Lane, Kettering, Northamptonshire NN16 4QT.</li>
    </ul>
  </section>
</body>
</html>
```